Creation of a Pinloom cover graphic

We need a Pinloom cover graphic for a page that will be used to test the market for an online training product.

The Product

The subject of the training is the basic online marketing. The training will be delivered online rather than at a venue.

The name of the website is www.groundworkpromo-hub.test. PLEASE NOTE We have owned the site domain for a while and the current content is 'NOT' representative of the new product. If Artvessel deliver on this project we will be back for the website and logo designs! please note we have included a draft logo concept file attachment with the brief.

Design Details

The cover graphic will be viewed on desktop, tablet and mobile. We have tried to give you a brief that guarantees the profile looks good and is readable on mobile. The design is bold and simple in order to enhance viewing the graphic on mobile.

We have included a draft graphic (Both as psd and png). This only shows layout and content. The draft graphic is mainly text based.

We have also included a concept file for the logo. You may want to incorporate the target and arrow icon contained in that file into the design.

Creating a design optimised for mobile is perhaps more challenging than larger formats. Feel free to designs with the following elements: Backgrounds; shapes; gradients and font/text effects - however try and retain a flat and simple design

Graphic size: 828px x 315px – we prefer this size rather than the mobile specific size. It actually renders best across all devices.
Place the design in between 174px & 650px horizontally as this gives best viewing on mobile. Backgrounds can extend across the whole graphic.
Web resolution

There are 2 section to the design:

Section 1. Title ‘The Brightpath Growth Team’
Section 2. Sub title ’Solving online marketing needs’ and to do listing

For the logo colouring and background we would prefer:

Background colour: #236d99 will be our main corporate colour. Other colours are #00456e, #236d99 and # 82bcd0.
Text colour : white or white with a shade of blue. You may contrast text colour of section 1 and section 2.

Fonts : We have two font styles in the draft (Arial Black and Arial Nova). The mobile first design requires the fonts to be very simple so as the text can be read on mobile devices. You can try similar such as Helvetica, Lato etc.
Icons etc : There are 3 ticks against each element of the to do list. Feel free to creative how you want to work with these.

Examples

The Artvessel graphic included in the files is a good example of simplicity and flat design.

Target Market(s)

Our clients will be business owners and managers. Generally, one person, small and medium sized businesses.
Gender : Both male and female.
Typical ages : 35-65
They favour simplicity, functionality and boldness - rather than elegance or sophistication

Industry/Entity Type

Marketing

Font styles to use
Sans Serif

Requirements
Must have
• View well on mobile devices
• Text readable on mobile devices
• Simplicity
• Flatter type of design
Nice to have
• Not really a design idea. Would like some feedback on whether our design brief was useful for you as designers.
Should not have
• Complex and finely detailed design

```html
<!DOCTYPE html>
<html lang="en">
<head>
<meta charset="utf-8">
<title>The Brightpath Growth Team – Pinloom Cover</title>
<link rel="stylesheet" href="https://fonts.googleapis.com/css2?family=Lato:wght@700;900&family=Open+Sans:wght@600;700&display=swap">
<style>
  :root {
    --page-bg: #e6e8ea;
    --brand-main: #236d99;
    --brand-deep: #00456e;
    --brand-navy: #003366;
    --brand-light: #82bcd0;
    --text-white: #ffffff;
    --text-soft: #e8f2f7;
    --icon-blue: #a9d2e0;
  }
  html, body {
    margin: 0;
    padding: 0;
    width: 1200px;
    height: 806px;
    overflow: hidden;
    background: var(--page-bg);
  }
  .cover-stage {
    width: 1200px;
    height: 806px;
    display: flex;
    align-items: center;
    justify-content: center;
  }
  .cover {
    display: block;
    width: 1200px;
    height: 456px;
  }
  .cover-title {
    font-family: "Lato", Arial, sans-serif;
    font-weight: 700;
    font-size: 38px;
    fill: var(--text-white);
  }
  .cover-subtitle {
    font-family: "Open Sans", Arial, sans-serif;
    font-weight: 600;
    font-size: 25px;
    fill: var(--brand-light);
  }
  .todo-item {
    font-family: "Open Sans", Arial, sans-serif;
    font-weight: 700;
    font-size: 19.5px;
    fill: var(--text-soft);
  }
  .target-icon circle {
    fill: none;
    stroke: var(--icon-blue);
    stroke-width: 2;
  }
  .target-icon .target-core {
    fill: var(--icon-blue);
    stroke: none;
  }
  .target-icon path {
    fill: none;
    stroke: var(--icon-blue);
    stroke-width: 2;
    stroke-linecap: round;
  }
</style>
</head>
<body>
<main class="cover-stage">
  <svg class="cover" viewBox="0 0 828 315" xmlns="http://www.w3.org/2000/svg" aria-labelledby="cover-heading">
    <defs>
      <linearGradient id="cover-fill" x1="0" y1="0" x2="0.25" y2="1">
        <stop offset="0" stop-color="#1c6a9c"/>
        <stop offset="0.55" stop-color="#0a5486"/>
        <stop offset="1" stop-color="#00386a"/>
      </linearGradient>
      <filter id="title-shadow" x="-10%" y="-30%" width="120%" height="160%">
        <feDropShadow dx="1" dy="2" stdDeviation="1.2" flood-color="#001b33" flood-opacity="0.75"/>
      </filter>
      <symbol id="target-arrow" viewBox="0 0 28 22">
        <g class="target-icon">
          <circle cx="17" cy="13" r="7"/>
          <circle cx="17" cy="13" r="3.5"/>
          <circle class="target-core" cx="17" cy="13" r="1.4"/>
          <path d="M17 13 L4 3"/>
          <path d="M4 3 L1 3.5 M4 3 L3.5 0 M7 5.3 L4 5.8 M7 5.3 L6.5 2.3"/>
        </g>
      </symbol>
    </defs>

    <rect class="cover-band" width="828" height="315" fill="url(#cover-fill)"/>

    <g class="cover-waves" fill="none" stroke="#ffffff">
      <path d="M0 40 C180 60 330 140 430 315" stroke-opacity="0.10" stroke-width="1.2"/>
      <path d="M0 70 C200 100 320 180 380 315" stroke-opacity="0.08" stroke-width="1"/>
      <path d="M190 0 C380 60 560 120 828 280" stroke-opacity="0.08" stroke-width="1"/>
      <path d="M500 0 C580 80 700 190 828 245" stroke-opacity="0.10" stroke-width="1.2"/>
      <path d="M0 40 C180 60 330 140 430 315 L0 315 Z" fill="#ffffff" fill-opacity="0.03" stroke="none"/>
      <path d="M500 0 C580 80 700 190 828 245 L828 0 Z" fill="#ffffff" fill-opacity="0.04" stroke="none"/>
    </g>

    <text id="cover-heading" class="cover-title" x="414" y="99" text-anchor="middle" filter="url(#title-shadow)">The Brightpath Growth Team</text>
    <text class="cover-subtitle" x="414" y="143" text-anchor="middle">Solving online marketing needs</text>

    <g class="todo-list">
      <use href="#target-arrow" x="280" y="163" width="28" height="22"/>
      <text class="todo-item" x="321" y="184">Making web sites ‘sticky’</text>
      <use href="#target-arrow" x="280" y="193" width="28" height="22"/>
      <text class="todo-item" x="321" y="214">Increasing conversions</text>
      <use href="#target-arrow" x="280" y="223" width="28" height="22"/>
      <text class="todo-item" x="321" y="244">Boosting quality traffic</text>
    </g>
  </svg>
</main>
</body>
</html>
```